Intuitive, look stunning website design for the street-level digital media platform that connects audiences with dynamic media on taxis and rideshare vehicles on BACK AND SIDE WINDOWS OF THE VEHICLE. SO FOOT TRAFFIC AND ALL OTHER TRAFFIC CAN SEE DISPLAY ON MOVING VEHICLE (in the future high glass building glass concept)
There should be 7 tabs VOLTANIX as home button, advertisers, partners, drivers, about us, news and contact.

Target Market(s)

The company works with taxi companies and rideshare drivers to install its proprietary advertising displays in their vehicles. These proprietary screens deliver dynamic content based on location-based, WiFi-enabled triggers.

Voltanix provides an additional revenue stream to maximize drive time and empowers brands to efficiently engage consumers across our nation's busiest cities, including San Francisco, Los Angeles, New York City, Dallas, Austin, Chicago and Miami.

Industry/Entity Type

Digital Marketing

Coding

Coded - Design and coding required

Number of Pages Required

5+ page

Font styles to use
Sans Serif

Requirements
Must have
• Use beautiful graphics and easy to read fonts.
Make sure graphics are compressed and optimized for fast loading.
Design should be consistent on brand throughout the website design.
Design an intuitive navigation system which allows users to get to the pages they need quickly.
Create pages that are standard for all business from small to big such; home, about us, product/services , sitemap ( seo purposes) contact us etc..
icons links for snapchat, instagram, client login, facbook
Nice to have
• Out of box concept
Should not have
• ITS NOT AN LCD BOX PLACED OVER THE CAR

```html
<!DOCTYPE html>
<html lang="en">
<head>
<meta charset="utf-8">
<title>Voltanix — Street-level digital media</title>
<link href="https://fonts.googleapis.com/css2?family=Poppins:wght@300;400;500;600;700&display=swap" rel="stylesheet">
<style>
:root{
  --blue:#1e8ad6;
  --blue-mid:#2f8fd0;
  --navy:#0d4f8b;
  --navy-deep:#0b4680;
  --slate:#4b6a86;
  --ink:#1b1b1b;
  --text:#555b62;
  --muted:#8a9096;
  --white:#ffffff;
  --line:#e3e6ea;
}
*{margin:0;padding:0;box-sizing:border-box}
html,body{width:1200px;height:4868px;overflow:hidden}
body{position:relative;font-family:"Poppins",sans-serif;color:var(--ink);background:var(--white)}
.abs{position:absolute}

/* hero */
.hero{left:0;top:0;width:1200px;height:820px;background:linear-gradient(115deg,#3a3d42 0%,#1c1d20 45%,#2b1e20 70%,#121315 100%)}
.hero-cut{left:0;top:700px;width:1200px;height:130px}
.brand{left:88px;top:40px;font-size:24px;font-weight:700;color:var(--white);letter-spacing:-.3px}
.nav{left:322px;top:46px;display:flex;gap:26px;list-style:none}
.nav a{color:var(--white);text-decoration:none;font-size:14px;font-weight:500}
.login{left:948px;top:34px;width:164px;height:46px;border:1.5px solid var(--white);border-radius:3px;color:var(--white);font-size:13px;font-weight:500;display:flex;align-items:center;justify-content:center}
.hero-title{left:88px;top:310px;font-size:60px;font-weight:700;line-height:64px;color:var(--white)}
.hero-title span{color:var(--blue)}
.hero-copy{left:88px;top:460px;width:460px;font-size:15px;line-height:22px;color:#e6e8ea}
.btn-outline{border:1.5px solid var(--white);color:var(--white);font-size:13px;font-weight:600;display:flex;align-items:center;justify-content:center}
.hero-btn{left:88px;top:534px;width:160px;height:46px}
.slide-count{left:1040px;top:482px;color:var(--white);font-size:44px;font-weight:700}
.slide-count small{font-size:20px;font-weight:400}

/* about */
.about-photo{left:88px;top:952px;width:492px;height:648px;background:linear-gradient(135deg,#c9ccd0,#8c9196 55%,#5c6166)}
.about-accent{left:560px;top:952px;width:20px;height:70px;background:var(--navy)}
.about-title{left:612px;top:1022px;width:500px;font-size:40px;line-height:48px;font-weight:700;color:var(--ink)}
.about-title .hl{color:var(--blue)}
.about-title .light{font-weight:300}
.about-copy{left:628px;top:1226px;width:470px;font-size:16px;line-height:27px;color:var(--text)}
.btn-blue-outline{border:2px solid var(--blue);color:var(--navy);background:var(--white);font-size:14px;font-weight:600;display:flex;align-items:center;justify-content:center;letter-spacing:.5px}
.about-btn{left:560px;top:1446px;width:192px;height:60px}

/* section titles */
.sec-title{left:0;width:1200px;text-align:center}
.sec-title h2{font-size:44px;font-weight:700;line-height:52px;color:var(--ink)}
.sec-title p{font-size:38px;font-weight:300;line-height:46px;color:var(--ink)}

/* services */
.services-head{top:1700px}
.service{top:1844px;width:332px;height:372px;color:var(--white);text-align:center;padding:0 34px}
.service svg{display:block;margin:62px auto 0}
.service h3{font-size:19px;font-weight:700;margin-top:22px}
.service p{font-size:13px;line-height:20px;margin-top:10px}
.svc-social{left:88px;background:var(--blue-mid)}
.svc-vehicle{left:432px;background:var(--navy)}
.svc-rideshare{left:780px;background:var(--slate)}

/* solutions */
.solutions-band{left:0;top:2468px;width:1200px;height:652px;background:linear-gradient(90deg,#1878c0 0%,#2a8fd4 45%,#5aaee3 100%)}
.solutions-photo{left:620px;top:2400px;width:580px;height:640px;background:linear-gradient(160deg,#8a8f95 0%,#5d6166 35%,#c9a21c 60%,#5a5d60 100%)}
.solutions-title{left:88px;top:2640px;width:520px;color:var(--white);font-size:40px;line-height:50px;font-weight:700}
.solutions-title span{font-weight:300;display:block}
.solutions-copy{left:88px;top:2782px;width:500px;color:#eef5fb;font-size:16px;line-height:25px}
.solutions-btn{left:88px;top:2946px;width:240px;height:58px}

/* news */
.news-head{top:3236px}
.card{top:3380px;width:332px;height:448px;background:var(--white);box-shadow:0 2px 10px rgba(0,0,0,.08)}
.card-photo{width:332px;height:232px}
.card-body{padding:24px 40px}
.card h3{font-size:16px;line-height:22px;font-weight:700}
.card p{font-size:12px;line-height:18px;color:var(--text);margin-top:14px}
.card .more{display:block;margin-top:12px;font-size:13px;font-weight:700;color:var(--navy)}
.card-1{left:88px}.card-1 .card-photo{background:linear-gradient(135deg,#3d4045,#6a2a2a 60%,#2a2c30)}
.card-2{left:432px}.card-2 .card-photo{background:linear-gradient(135deg,#6a6d70,#3b2628 55%,#8a8d90)}
.card-3{left:780px}.card-3 .card-photo{background:linear-gradient(135deg,#d9dcdf,#6e7378 55%,#3a3d41)}

/* partners */
.partners-head{top:3876px}
.partner-row{left:88px;top:4108px;width:1024px;height:80px;display:flex;border:1px solid var(--line)}
.partner{flex:1;border-right:1px solid var(--line);display:flex;align-items:center;justify-content:center}
.partner:last-child{border-right:none}
.partner i{display:block;width:110px;height:26px;border-radius:4px;background:#c9ced3}

/* footer */
.footer{left:0;top:4240px;width:1200px;height:628px;background:var(--navy-deep)}
.footer-cut{left:0;top:4238px;width:1200px;height:100px}
.footer-brand{left:88px;top:4486px;font-size:28px;font-weight:700;color:var(--white)}
.foot-col{top:4348px;color:var(--white)}
.foot-col h4{font-size:16px;font-weight:700;margin-bottom:14px}
.foot-col li{list-style:none;font-size:13px;line-height:23px}
.col-links{left:364px}
.col-news{left:560px}
.col-news p{font-size:13px;margin-bottom:14px}
.email-field{width:240px;height:40px;background:#2a64a0;color:#c9d7e6;font-size:12px;padding:0 14px;display:flex;align-items:center}
.subscribe{margin-top:14px;width:162px;height:40px;background:var(--blue);color:var(--white);font-size:13px;font-weight:600;display:flex;align-items:center;justify-content:center}
.col-contact{left:876px}
.col-contact li{display:flex;align-items:center;gap:8px}
.socials{display:flex;gap:8px;margin-top:14px}
.socials span{width:22px;height:22px;background:var(--white);border-radius:3px}
.foot-rule{left:88px;top:4804px;width:1024px;height:1px;background:rgba(255,255,255,.25)}
.copyright{left:0;top:4824px;width:1200px;text-align:center;color:var(--white);font-size:12px}
.to-top{left:1128px;top:4808px;width:40px;height:40px;border-radius:50%;background:var(--blue);display:flex;align-items:center;justify-content:center}
</style>
</head>
<body>

<!-- hero -->
<section class="hero abs" role="img" aria-label="Close-up of a dark car's rear light and back window at night"></section>
<svg class="hero-cut abs" viewBox="0 0 1200 130" preserveAspectRatio="none"><polygon points="0,120 1200,0 1200,130 0,130" fill="#fff"/></svg>
<div class="brand abs">Voltanix</div>
<ul class="nav abs">
  <li><a href="#">Advertisers</a></li><li><a href="#">Partners</a></li><li><a href="#">Drivers</a></li>
  <li><a href="#">About us</a></li><li><a href="#">News</a></li><li><a href="#">Contact</a></li>
</ul>
<div class="login abs">Client Login</div>
<h1 class="hero-title abs">Welcome to<br><span>Voltanix</span></h1>
<p class="hero-copy abs">The company works with taxi companies and rideshare drivers to install its proprietary advertising displays in their vehicles.</p>
<div class="hero-btn btn-outline abs">Get Started</div>
<div class="slide-count abs">01<small> /3</small></div>

<!-- about -->
<div class="about-photo abs" role="img" aria-label="Hands fitting a display panel to a car window"></div>
<div class="about-accent abs"></div>
<h2 class="about-title abs"><span class="hl">Voltanix</span>, a Digital Enterpreneur based in <span class="light">busiest cities</span>.</h2>
<p class="about-copy abs">Voltanix provides an additional revenue stream to maximize drive time and empowers brands to efficiently engage consumers across our nation's busiest cities, including San Francisco, Los Angeles, New York City, Dallas, Austin, Chicago and Miami.</p>
<div class="about-btn btn-blue-outline abs">ABOUT US</div>

<!-- services -->
<div class="sec-title services-head abs"><h2>Voltanix</h2><p>The best Services</p></div>
<div class="service svc-social abs">
  <svg width="70" height="70" viewBox="0 0 70 70" fill="none" stroke="#fff" stroke-width="3"><rect x="20" y="10" width="28" height="50" rx="4"/><line x1="30" y1="53" x2="38" y2="53"/><path d="M54 20a10 10 0 0 1 0 14M58 14a18 18 0 0 1 0 26"/></svg>
  <h3>Social Advertising</h3>
  <p>Lorem ipsum is simply dummy text of the printing and typesetting industry lorem ipsum has been.</p>
</div>
<div class="service svc-vehicle abs">
  <svg width="90" height="70" viewBox="0 0 90 70" fill="none" stroke="#fff" stroke-width="3"><path d="M10 46V36l10-4 12-12h26l12 12 10 4v10z"/><circle cx="26" cy="48" r="7" fill="#0d4f8b"/><circle cx="64" cy="48" r="7" fill="#0d4f8b"/><line x1="45" y1="20" x2="45" y2="32"/></svg>
  <h3>Vehicle Advertising</h3>
  <p>Lorem ipsum is simply dummy text of the printing and typesetting industry lorem ipsum has been.</p>
</div>
<div class="service svc-rideshare abs">
  <svg width="90" height="70" viewBox="0 0 90 70" fill="#fff"><rect x="36" y="10" width="22" height="10" rx="2"/><path d="M20 50V38l8-4 10-12h20l10 12 8 4v12z"/><circle cx="34" cy="52" r="6" fill="#4b6a86" stroke="#fff" stroke-width="3"/><circle cx="62" cy="52" r="6" fill="#4b6a86" stroke="#fff" stroke-width="3"/></svg>
  <h3>Rideshare vehicles</h3>
  <p>Lorem ipsum is simply dummy text of the printing and typesetting industry lorem ipsum has been.</p>
</div>

<!-- solutions -->
<div class="solutions-band abs"></div>
<div class="solutions-photo abs" role="img" aria-label="Yellow taxi cabs in city traffic"></div>
<h2 class="solutions-title abs">Voltanix, We offer <span>advertising solutions</span></h2>
<p class="solutions-copy abs">Lorem ipsum is simply dummy text of the printing and typesetting industry. Lorem ipsum has been the industry's standard dummy text ever since the 1500s, when an unknown printer took a galley of type and scrambled it to make...</p>
<div class="solutions-btn btn-outline abs">FOR ADVERTISER</div>

<!-- news -->
<div class="sec-title news-head abs"><h2>Our news</h2><p>From the Blog</p></div>
<article class="card card-1 abs"><div class="card-photo" role="img" aria-label="Rear of a dark car with tail light"></div><div class="card-body"><h3>Planning on the strategy from figures</h3><p>Lorem ipsum is simply dummy text of the printing and typesetting industry lorem ipsum has been.</p><span class="more">READ MORE</span></div></article>
<article class="card card-2 abs"><div class="card-photo" role="img" aria-label="Back window of a parked car"></div><div class="card-body"><h3>Planning on the strategy from figures</h3><p>Lorem ipsum is simply dummy text of the printing and typesetting industry lorem ipsum has been.</p><span class="more">READ MORE</span></div></article>
<article class="card card-3 abs"><div class="card-photo" role="img" aria-label="Driver standing beside a car on the street"></div><div class="card-body"><h3>Planning on the strategy from figures</h3><p>Lorem ipsum is simply dummy text of the printing and typesetting industry lorem ipsum has been.</p><span class="more">READ MORE</span></div></article>

<!-- partners -->
<div class="sec-title partners-head abs"><h2>Voltanix</h2><p>Partner</p></div>
<div class="partner-row abs">
  <div class="partner" aria-label="Partner badge"><i></i></div>
  <div class="partner" aria-label="Partner badge"><i></i></div>
  <div class="partner" aria-label="Partner badge"><i></i></div>
  <div class="partner" aria-label="Partner badge"><i></i></div>
  <div class="partner" aria-label="Partner badge"><i></i></div>
</div>

<!-- footer -->
<footer class="footer abs"></footer>
<svg class="footer-cut abs" viewBox="0 0 1200 100" preserveAspectRatio="none"><polygon points="0,0 1200,0 0,90" fill="#fff"/></svg>
<div class="footer-brand abs">Voltanix</div>
<div class="foot-col col-links abs"><h4>Useful Links</h4><ul><li>Advertisers</li><li>Partners</li><li>Drivers</li><li>About us</li><li>News</li><li>Contact</li><li>Site map</li></ul></div>
<div class="foot-col col-news abs"><h4>Newsletter</h4><p>Subscribe to our newsletter</p><div class="email-field">Email Address</div><div class="subscribe">SUBSCRIBE</div></div>
<div class="foot-col col-contact abs"><h4>Contact Us</h4>
  <ul>
    <li><svg width="12" height="14" viewBox="0 0 12 14" fill="#fff"><path d="M6 0a5 5 0 0 1 5 5c0 4-5 9-5 9S1 9 1 5a5 5 0 0 1 5-5z"/></svg>Some goes address here</li>
    <li><svg width="12" height="10" viewBox="0 0 12 10" fill="none" stroke="#fff" stroke-width="1.5"><rect x="1" y="1" width="10" height="8"/><path d="M1 1l5 4 5-4"/></svg>info@voltanix.com</li>
    <li><svg width="12" height="12" viewBox="0 0 12 12" fill="#fff"><path d="M2 0h3l1 3-2 1a7 7 0 0 0 4 4l1-2 3 1v3c0 1-1 2-2 2A11 11 0 0 1 0 2c0-1 1-2 2-2z"/></svg>(555) 014-2260</li>
    <li><svg width="12" height="12" viewBox="0 0 12 12" fill="none" stroke="#fff" stroke-width="1.3"><circle cx="6" cy="6" r="5"/><path d="M1 6h10M6 1c3 3 3 7 0 10M6 1c-3 3-3 7 0 10"/></svg>www.voltanix.com</li>
  </ul>
  <div class="socials" aria-label="Social links"><span></span><span></span><span></span></div>
</div>
<div class="foot-rule abs"></div>
<div class="copyright abs">Copyright 2020 | All Rights Reserved</div>
<div class="to-top abs"><svg width="14" height="10" viewBox="0 0 14 10" fill="none" stroke="#fff" stroke-width="2"><path d="M1 9l6-7 6 7"/></svg></div>

</body>
</html>
```